Dog care service needs advertising poster

Our company is Paw Haven. We provide care for dogs while their owners are away, either through home visits or a holiday stay in the homes of carefully selected minders. Our existing website & Facebook cover should provide all the colour cues for a poster - namely blues, blondes and grey. We have an existing logo (provided). We can feature the same imagery from our website as I have purchased the rights to the stock images.

www.pawhavenexample.com.au
www.facebook.com/pawhavenexampleau

This brief is for design of a poster that can be placed in vet surgeries, groomers, on community noticeboards. It should be scalable to print in three sizes, A5, A4 & A3.

We wish to clearly communicate our three areas of service "dog minding, home visits, dog walking".

We would like to have the files ready for upload to Printora (or similar) for immediate printing.

Target Market(s)

Dog owners who love their dogs like family.

Industry/Entity Type

Advertising

Font styles to use
Sans Serif

Colors
33a6d7
3276b5

Requirements
Must have
• Logo
• www.pawhavenexample.com.au
• Telephone number
• Three services - Dog Minding, Home Visits, Dog Walking
Nice to have
• use of our existing stock photography to highlight the three areas of service - Dog minding, home visits, dog walking. Existing colour palette - blues, blondes and grey.
• Text that can be used:
• Western Sydney’s complete dog care service.
• Dog Minding - Your dog stays in the home of one of our carefully selected minders.Treated like part of the family, they enjoy all the creature comforts they are used to.
• Home Visits - We visit your dog at your home for feeding, walking and playtime. Short of long visits available.
• Dog Walking - If you can't walk your dog for any reason we are here to help. 1/2 hour or hourly walks available.
• Contact us today for a tailored package to meet your needs.
Should not have
• Any additional illustrations beyond the logo.

```html
<!DOCTYPE html>
<html lang="en">
<head>
<meta charset="utf-8">
<title>Paw Haven – Dog Care Poster</title>
<link rel="stylesheet" href="https://fonts.googleapis.com/css2?family=Raleway:wght@600;700;800&family=Open+Sans:wght@400;600&display=swap">
<style>
  :root {
    --stage: #e4e4e4;
    --slate: #3a4557;
    --sky-blue: #33a6d7;
    --deep-blue: #3276b5;
    --band-blue: #1e8fcd;
    --white: #ffffff;
    --body-grey: #4d5560;
    --sky-top: #d7dde2;
    --sky-mid: #bfcdd6;
    --sea: #4f86ad;
    --sand: #c9a77a;
  }
  * { box-sizing: border-box; margin: 0; padding: 0; }
  html, body { width: 1200px; height: 789px; overflow: hidden; }
  body { background: var(--stage); font-family: "Open Sans", Arial, sans-serif; }

  .poster {
    position: absolute; left: 338px; top: 24px;
    width: 524px; height: 741px;
    background: var(--white); overflow: hidden;
    box-shadow: 0 4px 14px rgba(0,0,0,.18);
  }
  .poster__top-rule { position: absolute; top: 0; left: 0; right: 0; height: 8px; background: var(--slate); }

  .hero-photo {
    position: absolute; top: 8px; left: 0; right: 0; height: 582px;
    background:
      linear-gradient(to bottom, var(--sky-top) 0%, var(--sky-mid) 45%, var(--sea) 56%, #3f79a3 72%, var(--sand) 78%, #b8935f 100%);
  }
  .hero-photo__dog {
    position: absolute; left: 235px; top: 220px; width: 170px; height: 330px;
    background: radial-gradient(ellipse at 50% 40%, #d9b572 0%, #c99d55 60%, rgba(201,157,85,0) 75%);
  }

  .brand-tab {
    position: absolute; top: 8px; left: 50%; transform: translateX(-50%);
    width: 180px; height: 64px; background: var(--white);
    border-radius: 0 0 14px 14px;
    display: flex; align-items: center; justify-content: center; gap: 10px;
    box-shadow: 0 2px 6px rgba(0,0,0,.12);
  }
  .brand-tab__mark { width: 22px; height: 22px; border-radius: 50%; background: var(--deep-blue); }
  .brand-tab__name { font-family: "Raleway", Arial, sans-serif; font-weight: 700; font-size: 22px; color: var(--slate); }

  .headline {
    position: absolute; top: 100px; left: 0; right: 0; text-align: center;
    font-family: "Raleway", Arial, sans-serif; font-weight: 800; letter-spacing: .5px;
  }
  .headline__line { display: block; font-size: 25px; line-height: 30px; color: var(--slate); }
  .headline__line--accent { color: var(--band-blue); }

  .service-card {
    position: absolute; top: 330px; width: 150px; background: var(--white);
    padding: 7px 7px 12px; box-shadow: 0 3px 8px rgba(0,0,0,.25);
  }
  .service-card--minding { left: 26px; transform: rotate(-3deg); top: 336px; }
  .service-card--visits  { left: 187px; top: 326px; }
  .service-card--walking { left: 348px; transform: rotate(3deg); top: 336px; }
  .service-card__photo { height: 100px; }
  .service-card--minding .service-card__photo { background: linear-gradient(to bottom, #7fae4a, #4d7f2c); }
  .service-card--visits .service-card__photo { background: linear-gradient(to bottom, #e9e6df 0%, #d8d2c6 45%, #8c6a45 55%, #6f5133 100%); }
  .service-card--walking .service-card__photo { background: linear-gradient(to bottom, #6e9a5a 0%, #4f8a3e 40%, #5aa23f 100%); }
  .service-card__title {
    font-family: "Raleway", Arial, sans-serif; font-weight: 700; font-size: 15px;
    color: var(--band-blue); text-align: center; margin: 7px 0 4px;
  }
  .service-card__text { font-size: 8.5px; line-height: 11px; color: var(--body-grey); text-align: center; }

  .contact-band {
    position: absolute; left: 0; right: 0; top: 590px; height: 141px;
    background: var(--band-blue); color: var(--white);
  }
  .contact-band__pitch {
    position: absolute; left: 44px; top: 28px;
    font-family: "Raleway", Arial, sans-serif; font-weight: 700; font-size: 17px; line-height: 21px;
  }
  .contact-band__details { position: absolute; left: 262px; top: 40px; }
  .contact-line { display: flex; align-items: center; gap: 12px; margin-bottom: 14px;
    font-family: "Raleway", Arial, sans-serif; font-weight: 700; }
  .contact-line--phone { font-size: 18px; }
  .contact-line--web { font-size: 14px; }
  .contact-line svg { width: 18px; height: 18px; flex: none; }
  .poster__bottom-rule { position: absolute; bottom: 0; left: 0; right: 0; height: 10px; background: var(--slate); }
</style>
</head>
<body>
  <main class="poster">
    <div class="hero-photo" role="img" aria-label="Photograph of a golden labrador sitting on a sandy beach by the sea">
      <div class="hero-photo__dog"></div>
    </div>
    <div class="poster__top-rule"></div>

    <div class="brand-tab">
      <span class="brand-tab__mark"></span>
      <span class="brand-tab__name">Paw Haven</span>
    </div>

    <h1 class="headline">
      <span class="headline__line">WESTERN SYDNEY’S COMPLETE</span>
      <span class="headline__line headline__line--accent">DOG CARE SERVICE</span>
    </h1>

    <section class="service-card service-card--minding">
      <div class="service-card__photo" role="img" aria-label="Photograph of a dog resting on green grass"></div>
      <h2 class="service-card__title">Dog Minding</h2>
      <p class="service-card__text">Your dog stays in the home of one of our carefully selected minders. Treated like part of the family, they enjoy all the creature comforts they are used to.</p>
    </section>

    <section class="service-card service-card--visits">
      <div class="service-card__photo" role="img" aria-label="Photograph of a small dog sitting on a home doormat"></div>
      <h2 class="service-card__title">Home Visits</h2>
      <p class="service-card__text">We visit your dog at your home for feeding, walking and playtime. Short of long visits available.</p>
    </section>

    <section class="service-card service-card--walking">
      <div class="service-card__photo" role="img" aria-label="Photograph of a bulldog on a lead on a lawn"></div>
      <h2 class="service-card__title">Dog Walking</h2>
      <p class="service-card__text">If you can't walk your dog for any reason we are here to help. 1/2 hour or hourly walks available.</p>
    </section>

    <footer class="contact-band">
      <p class="contact-band__pitch">Contact us today<br>for a tailored package<br>to meet your needs.</p>
      <div class="contact-band__details">
        <div class="contact-line contact-line--phone">
          <svg viewBox="0 0 24 24" aria-hidden="true"><path fill="#fff" d="M6.6 10.8a15.1 15.1 0 0 0 6.6 6.6l2.2-2.2c.3-.3.7-.4 1-.2 1.1.4 2.3.6 3.6.6.6 0 1 .4 1 1V20c0 .6-.4 1-1 1A17 17 0 0 1 3 4c0-.6.4-1 1-1h3.5c.6 0 1 .4 1 1 0 1.3.2 2.5.6 3.6.1.3 0 .7-.2 1z"/></svg>
          <span>0400 555 128</span>
        </div>
        <div class="contact-line contact-line--web">
          <svg viewBox="0 0 24 24" aria-hidden="true"><rect x="2" y="3" width="20" height="14" rx="1" fill="none" stroke="#fff" stroke-width="2"/><rect x="10" y="17" width="4" height="3" fill="#fff"/><rect x="7" y="20" width="10" height="2" fill="#fff"/></svg>
          <span>www.pawhavenexample.com.au</span>
        </div>
      </div>
    </footer>
    <div class="poster__bottom-rule"></div>
  </main>
</body>
</html>
```